Fireworks company

COLORFUL design, incorporating logo (attached).
Information to be included:
PO BOX 4829
Marlow Vale 3891
Ph 03 5461 8237
Fax 03 5387 9216
Email sales@brindarockets.com.au
Web www.brindarockets.com.au

Check out our website for more inspiration? :-)

```html
<!DOCTYPE html>
<html lang="en">
<head>
<meta charset="utf-8">
<title>Brinda Rockets Letterhead</title>
<link rel="stylesheet" href="https://fonts.googleapis.com/css2?family=Open+Sans:wght@400&family=Source+Sans+3:wght@400;700&display=swap">
<style>
  :root {
    --backdrop: #efece8;
    --paper: #ffffff;
    --brand-orange: #ff4a0a;
    --accent-orange: #ff8a00;
    --accent-red: #d8141c;
    --brown: #4a2210;
    --ink: #222222;
    --rule: #555555;
    --glow-warm: #fff4c8;
    --glow-pink: #fbe0dc;
  }
  html, body {
    margin: 0;
    padding: 0;
    width: 943px;
    height: 1200px;
    overflow: hidden;
    background: var(--backdrop);
  }
  .letterhead {
    position: absolute;
    left: 57px;
    top: 65px;
    width: 828px;
    height: 1071px;
    background: var(--paper);
    box-shadow: 0 2px 8px rgba(0,0,0,0.25);
    overflow: hidden;
  }
  .brand {
    position: absolute;
    left: 20px;
    top: 42px;
    display: flex;
    align-items: center;
    gap: 12px;
  }
  .brand-name {
    font-family: "Source Sans 3", sans-serif;
    font-weight: 700;
    font-size: 38px;
    line-height: 1;
    letter-spacing: 1px;
    color: var(--brand-orange);
    text-transform: uppercase;
  }
  .brand-dot {
    width: 22px;
    height: 22px;
    border-radius: 50%;
    background: var(--brand-orange);
  }
  .contact {
    position: absolute;
    left: 544px;
    top: 37px;
    padding-left: 18px;
    border-left: 1px solid var(--rule);
    font-family: "Source Sans 3", sans-serif;
    font-size: 15.5px;
    line-height: 23px;
    color: var(--ink);
    margin: 0;
    list-style: none;
  }
  .contact li {
    display: flex;
    align-items: center;
    gap: 6px;
  }
  .contact svg {
    width: 13px;
    height: 13px;
    fill: var(--ink);
    flex: none;
  }
  .backdrop-glow {
    position: absolute;
    left: 168px;
    top: 375px;
    width: 480px;
    height: 450px;
    border-radius: 50%;
    background: radial-gradient(circle, var(--glow-warm) 0%, rgba(255,244,200,0.5) 35%, rgba(251,224,220,0.35) 60%, rgba(255,255,255,0) 72%);
  }
  .footer-wave {
    position: absolute;
    left: 0;
    bottom: 0;
    width: 828px;
    height: 100px;
    display: block;
  }
  .postal {
    position: absolute;
    left: 0;
    bottom: 12px;
    width: 390px;
    text-align: center;
    font-family: "Open Sans", sans-serif;
    font-size: 16.5px;
    line-height: 22px;
    letter-spacing: 0.8px;
    color: #ffffff;
    margin: 0;
  }
</style>
</head>
<body>
  <main class="letterhead">
    <header>
      <div class="brand">
        <span class="brand-name">Brinda<br>Rockets</span>
        <span class="brand-dot"></span>
      </div>
      <ul class="contact">
        <li>
          <svg viewBox="0 0 16 16" aria-label="Phone"><path d="M3.5 1l2.5 3-1.5 1.8c.8 2 2.2 3.4 4.2 4.2L10.5 8.5l3 2.5-1.2 3C7 13.8 2.2 9 2 3.5z"/></svg>
          03 5461 8237
        </li>
        <li>
          <svg viewBox="0 0 16 16" aria-label="Fax"><path d="M4 1h7v4H4zM1 6h14v7h-2v2H3v-2H1zM4 10v4h8v-4z"/></svg>
          03 5387 9216
        </li>
        <li>
          <svg viewBox="0 0 16 16" aria-label="Email"><path d="M1 3h14v1.5L8 9 1 4.5zM1 6.2l7 4.5 7-4.5V13H1z"/></svg>
          sales@brindarockets.com.au
        </li>
        <li>
          <svg viewBox="0 0 16 16" aria-label="Web"><path d="M8 1a7 7 0 100 14A7 7 0 008 1zm0 1.5c.9 0 1.8 1.6 2.1 4H5.9C6.2 4.1 7.1 2.5 8 2.5zM2.6 6.5h2c-.1.5-.1 1-.1 1.5s0 1 .1 1.5h-2a5.6 5.6 0 010-3zm3.3 3h4.2C9.8 11.9 8.9 13.5 8 13.5S6.2 11.9 5.9 9.5zm5.5 0c.1-.5.1-1 .1-1.5s0-1-.1-1.5h2a5.6 5.6 0 010 3z"/></svg>
          www.brindarockets.com.au
        </li>
      </ul>
    </header>

    <div class="backdrop-glow" role="img" aria-label="Faint brand emblem in soft yellow and pink"></div>

    <footer>
      <svg class="footer-wave" viewBox="0 0 828 100" preserveAspectRatio="none" aria-hidden="true">
        <path fill="var(--accent-red)" d="M460,30 C620,45 740,30 828,2 L828,14 C740,40 620,50 460,32 Z"/>
        <path fill="var(--accent-orange)" d="M470,36 C630,54 750,44 828,22 L828,52 C740,68 600,62 470,38 Z"/>
        <path fill="var(--brown)" d="M0,36 C200,-4 360,10 520,40 C620,58 740,70 828,56 L828,64 C740,78 630,70 520,48 C360,18 200,4 0,43 Z"/>
        <path fill="var(--brand-orange)" d="M0,48 C200,12 360,24 520,54 C640,76 740,84 828,72 L828,100 L0,100 Z"/>
      </svg>
      <p class="postal">PO BOX 4829<br>Marlow Vale 3891</p>
    </footer>
  </main>
</body>
</html>
```